Tamborine Ridge Country Club Business Sponsorship Package

Need a flyer to promote new business sponsorship packageCost 4500 + GST12 months sponsorship and promotion via TRCC Corporate Partners listing $1000 Food & Beverage House AccountMembers Welcome PackChristmas Party Invite7 Day with Cart Golf Membership10% discount on events and showsPayable over 4 installments

Target Market(s)

Business Owners who play Golf

Industry/Entity Type

Golf Course

```html
<!DOCTYPE html>
<html lang="en">
<head>
<meta charset="utf-8">
<title>Tamborine Ridge Country Club – Business Sponsorship Package</title>
<link href="https://fonts.googleapis.com/css2?family=Bebas+Neue&family=Cinzel:wght@600&display=swap" rel="stylesheet">
<style>
  :root {
    --backdrop: #2c2e30;
    --paper: #e3e3e3;
    --ink: #1c1c1c;
    --heading-grey: #3b3b3b;
    --green-deep: #15664a;
    --green-mid: #1f7a58;
    --green-soft: #5aa087;
    --green-soft-light: #6aae95;
    --white: #ffffff;
  }
  * { margin: 0; padding: 0; box-sizing: border-box; }
  html, body { width: 1200px; height: 1200px; overflow: hidden; }
  body { background: var(--backdrop); position: relative; font-family: "Bebas Neue", "Arial Narrow", sans-serif; }

  .flyer {
    position: absolute; left: 195px; top: 27px;
    width: 810px; height: 1146px;
    background: var(--paper);
    overflow: hidden;
  }

  .club-header {
    position: absolute; left: 0; top: 66px; width: 100%;
    display: flex; align-items: center; justify-content: center; gap: 22px;
    font-family: "Cinzel", Georgia, serif; font-weight: 600;
    font-size: 33px; color: var(--ink); letter-spacing: 0.5px;
  }
  .club-mark { width: 34px; height: 34px; background: var(--green-deep); }

  .hero-photo {
    position: absolute; left: 30px; top: 150px; width: 780px; height: 560px;
    background: radial-gradient(ellipse 38% 45% at 45% 55%, #5a5a5a 0%, #8d8d8d 35%, rgba(200,200,200,0.5) 65%, rgba(227,227,227,0) 100%);
  }

  .card {
    position: absolute; border-radius: 12px; overflow: hidden;
    box-shadow: 0 14px 18px -10px rgba(0,0,0,0.35);
    text-align: center; color: var(--white);
  }
  .card--side { top: 685px; width: 181px; height: 377px;
    background: linear-gradient(180deg, var(--green-mid), var(--green-deep)); }
  .card--left { left: 89px; }
  .card--right { left: 540px; }
  .card--feature { left: 270px; top: 626px; width: 270px; height: 491px; z-index: 2;
    background: linear-gradient(180deg, var(--green-soft-light), var(--green-soft)); }

  .card__cap {
    position: absolute; left: 0; top: 0; width: 100%;
    background: linear-gradient(180deg, #ffffff 60%, #efefef);
  }
  .card--side .card__cap { height: 172px; clip-path: polygon(0 0, 100% 0, 100% 124px, 50% 172px, 0 124px); }
  .card--feature .card__cap { height: 223px; clip-path: polygon(0 0, 100% 0, 100% 163px, 50% 223px, 0 163px); }

  .card__title { position: absolute; left: 0; width: 100%; color: var(--heading-grey); line-height: 1; }
  .card--side .card__title { font-size: 35px; }
  .card--feature .card__title { font-size: 46px; line-height: 59px; top: 33px; }

  .card__body { position: absolute; left: 0; width: 100%; line-height: 1; }
  .price { font-size: 58px; }
  .fine { font-size: 20px; line-height: 24px; }
  .fine--small { font-size: 17px; line-height: 21px; }
  .cost-label { font-size: 25px; text-align: left; padding-left: 51px; }
  .cost-value { font-size: 84px; letter-spacing: -1px; }
  .cost-tax { font-size: 24px; }
  .term { font-size: 38px; line-height: 40px; }
  .discount-big { font-size: 52px; }
  .discount-word { font-size: 28px; }
</style>
</head>
<body>
  <main class="flyer">
    <header class="club-header">
      <span>Tamborine Ridge</span>
      <span class="club-mark" aria-hidden="true"></span>
      <span>Country Club</span>
    </header>

    <div class="hero-photo" role="img" aria-label="Golfer in white cap and polo at the top of his swing, with a burst of dark smoke and flying particles behind him"></div>

    <section class="card card--side card--left">
      <div class="card__cap"></div>
      <div class="card__title" style="top:22px; line-height:40px;">Corporate<br>Partners<br>Listing</div>
      <div class="card__body price" style="top:198px;">$1000</div>
      <div class="card__body fine" style="top:258px;">Food &amp; Beverage<br>House Account<br>Members</div>
    </section>

    <section class="card card--feature">
      <div class="card__cap"></div>
      <div class="card__title">Sponsorship<br>Package</div>
      <div class="card__body cost-label" style="top:236px;">Cost</div>
      <div class="card__body" style="top:258px;"><span class="cost-value">4500</span> <span class="cost-tax">+ GST</span></div>
      <div class="card__body term" style="top:335px;">12 Months<br>Sponsorship</div>
    </section>

    <section class="card card--side card--right">
      <div class="card__cap"></div>
      <div class="card__title" style="top:57px;">Membership</div>
      <div class="card__body" style="top:192px;"><span class="discount-big">10%</span> <span class="discount-word">Discount</span></div>
      <div class="card__body fine fine--small" style="top:247px;">On events and<br>shows payable over<br>4 installments</div>
    </section>
  </main>
</body>
</html>
```